Design a helpdesk ticketing platform *

We are launching a helpdesk ticketing platform. Very much like quellbox.com, merrylark.com, pivolta.com, brisktray.com etc. We have a full mid-fidelity prototype built and we want someone to build the full fidelity of the product.

You can view the full mid-fidelity prototype here: https://lnk.vexora.net/Qa8Lpw

The best way moving forward is to just design the following 4 pages

- Main Dashboard https://lnk.vexora.net/81hRtd
- All tickets https://lnk.vexora.net/jwNoEb
- Viewing a ticket https://lnk.vexora.net/Ys4VmK
- Contacts https://lnk.vexora.net/pHeXuo

Target Market(s)

Small business owners

Industry/Entity Type

Saas

Number of Pages Required

4 page

Font styles to use
Serif
Sans Serif

Colors

Designer to choose colors to be used in the design.

Requirements
Must have
• Must follow the prototype exactly. We are not looking for any UX changes. We want the designe xactly as the prototype is. We are only looking for design ideas.
Should not have
• modern, clean. We'd love to see the primary color as yellow, purple, orange, green or blue. You choose which one you think looks best and go with that.

```html
<!DOCTYPE html>
<html lang="en">
<head>
<meta charset="utf-8">
<title>Ticketgrove – All Tickets</title>
<link href="https://fonts.googleapis.com/css2?family=Roboto:wght@400;500&display=swap" rel="stylesheet">
<style>
:root{
  --brand:#06bd8b;
  --brand-active:#0fe2a9;
  --brand-accent:#12efb3;
  --submenu:#d3dcd9;
  --submenu-active:#f7fbe5;
  --canvas:#f8fce7;
  --topbar:#cddadb;
  --tab-mid:#cddadb;
  --tab-dark:#c1d1d3;
  --row-selected:#cddadb;
  --ink:#1f2b2b;
  --ink-soft:#3a4646;
  --link:#06bd8b;
  --white:#ffffff;
  --rule:#cdd6d2;
  --squeeze:.5;
}
*{box-sizing:border-box;margin:0;padding:0}
html,body{width:1200px;height:675px;overflow:hidden}
body{font-family:"Roboto",Arial,sans-serif;text-transform:uppercase;color:var(--ink);background:var(--canvas);position:relative}

/* condensed label: narrow display lettering */
.label{display:inline-block;white-space:nowrap;transform:scaleX(var(--squeeze));transform-origin:left center}
.label.center{transform-origin:center center}

.sidebar{position:absolute;left:0;top:0;width:244px;height:675px;background:var(--brand);color:var(--white)}
.brand-name{position:absolute;left:37px;top:30px;font-size:31px;font-weight:500;line-height:1}
.nav-item{position:absolute;left:0;width:244px;display:flex;align-items:center;padding-left:37px;font-size:18px;gap:10px}
.nav-item svg{flex:none;width:20px;height:20px;stroke:var(--white);fill:none;stroke-width:1.4}
.nav-item.active{background:var(--brand-active);height:48px;top:146px}
.nav-more{position:absolute;right:0;top:0;width:28px;height:48px;background:var(--brand-accent);display:flex;flex-direction:column;align-items:center;justify-content:center;gap:3px}
.nav-more i{width:3px;height:3px;border-radius:50%;background:var(--white)}
.nav-sep{position:absolute;left:19px;width:207px;height:1px;background:rgba(255,255,255,.35)}
.submenu{position:absolute;left:0;top:194px;width:244px;height:144px;background:var(--submenu)}
.submenu-item{position:absolute;left:0;width:244px;padding-left:38px;display:flex;align-items:center;font-size:15px;color:var(--ink-soft)}
.submenu-item.current{background:var(--submenu-active);color:var(--ink)}
.submenu-sep{position:absolute;left:19px;width:207px;height:1px;background:#bfc9c6}
.create-btn{position:absolute;left:27px;top:505px;width:191px;height:38px;background:var(--white);border-radius:4px;color:var(--brand);font-size:14.5px;display:flex;align-items:center;justify-content:center}

.topbar{position:absolute;left:244px;top:0;width:956px;height:38px;background:var(--topbar)}
.avatar{position:absolute;left:20px;top:9px;width:20px;height:20px;border-radius:50%;background:linear-gradient(#a9b6c0,#6b7a86);border:1.5px solid var(--white)}
.user-name{position:absolute;left:48px;top:12px;font-size:12px;line-height:14px;color:var(--ink-soft)}
.search-icon{position:absolute;left:815px;top:11px;width:15px;height:15px}
.topbar-divider{position:absolute;left:846px;top:0;width:1px;height:38px;background:#aebcbd}
.account-link{position:absolute;left:866px;top:12px;font-size:12px;line-height:14px;color:var(--ink-soft)}

.tabs{position:absolute;left:244px;top:38px;height:29px;display:flex}
.tab{height:29px;display:flex;align-items:center;justify-content:center;font-size:15px;color:var(--ink-soft)}
.tab.tickets{width:51px;background:var(--canvas)}
.tab.all{width:69px;background:var(--tab-mid)}
.tab.mine{width:65px;background:var(--tab-dark)}
.filter-icon{position:absolute;left:1161px;top:46px;width:20px;height:20px}

.table{position:absolute;left:262px;top:80px;width:920px;font-size:11px;color:var(--ink-soft)}
.row{position:absolute;left:0;width:920px;height:56px}
.row.head{top:0;height:27px;border-bottom:1px solid var(--rule);color:var(--ink);font-size:12px}
.row.selected{background:var(--row-selected)}
.cell{position:absolute;top:50%;transform:translateY(-50%);white-space:nowrap;line-height:1}
.check{left:16px;width:8px;height:8px;border:1.4px solid var(--ink);border-radius:2px}
.star{left:45px;width:14px;height:14px}
.initials{left:74px;width:20px;height:20px;border-radius:50%;display:flex;align-items:center;justify-content:center;font-size:10px}
.selected .initials{background:var(--submenu-active)}
.contact{left:106px;font-size:15.5px;color:var(--ink)}
.date{left:202px}
.num{left:284px;color:var(--link)}
.subject{left:314px}
.state{left:468px}
.group{left:516px}
.agent{left:556px}
.priority{left:602px}
</style>
</head>
<body>
<aside class="sidebar">
  <div class="brand-name"><span class="label">Ticketgrove</span></div>

  <div class="nav-item" style="top:107px;height:28px">
    <svg viewBox="0 0 20 20"><circle cx="10" cy="10" r="8.5"/><path d="M10 10l3-4M5 10h1.5M13.5 10H15M10 4.5V6"/></svg>
    <span class="label">Dashboard</span>
  </div>

  <div class="nav-item active">
    <svg viewBox="0 0 20 20"><path d="M2 7l13-3 1 3a2 2 0 000 3l1 3-13 3-1-3a2 2 0 000-3z"/><path d="M6 9l6-1.5M6.5 11.5l6-1.5"/></svg>
    <span class="label">Tickets</span>
    <div class="nav-more"><i></i><i></i><i></i></div>
  </div>

  <div class="submenu">
    <div class="submenu-item current" style="top:0;height:36px"><span class="label">All tickets</span></div>
    <div class="submenu-item" style="top:36px;height:36px"><span class="label">My tickets</span></div>
    <div class="submenu-sep" style="top:72px"></div>
    <div class="submenu-item" style="top:72px;height:35px"><span class="label">Open tickets</span></div>
    <div class="submenu-sep" style="top:107px"></div>
    <div class="submenu-item" style="top:107px;height:37px"><span class="label">Unassigned tickets</span></div>
  </div>

  <div class="nav-item" style="top:350px;height:28px">
    <svg viewBox="0 0 20 20"><rect x="1.5" y="4" width="17" height="12" rx="1"/><circle cx="13" cy="8.5" r="1.8"/><path d="M10 13.5c.5-2 5.5-2 6 0M4 8h4M4 11h4"/></svg>
    <span class="label">Contacts</span>
  </div>
  <div class="nav-sep" style="top:389px"></div>

  <div class="nav-item" style="top:399px;height:28px">
    <svg viewBox="0 0 20 20"><rect x="1.5" y="3" width="17" height="6" rx="3"/><rect x="1.5" y="11" width="17" height="6" rx="3"/><circle cx="5" cy="6" r="1.5"/><circle cx="15" cy="14" r="1.5"/></svg>
    <span class="label">Admin settings</span>
  </div>
  <div class="nav-sep" style="top:438px"></div>

  <div class="nav-item" style="top:448px;height:28px">
    <svg viewBox="0 0 20 20"><rect x="1.5" y="4" width="17" height="12" rx="1"/><path d="M1.5 8h17M4 12.5h5"/></svg>
    <span class="label">Account &amp; billing</span>
  </div>

  <div class="create-btn"><span class="label center">+ Create a new ticket</span></div>
</aside>

<header class="topbar">
  <div class="avatar" role="img" aria-label="User profile photo"></div>
  <span class="user-name"><span class="label">Marcus Delane</span></span>
  <svg class="search-icon" viewBox="0 0 15 15" fill="none" stroke="#2b3636" stroke-width="1.4"><circle cx="6" cy="6" r="4.8"/><path d="M9.5 9.5L14 14"/></svg>
  <div class="topbar-divider"></div>
  <span class="account-link"><span class="label">My account &amp; billing</span></span>
</header>

<nav class="tabs">
  <div class="tab tickets"><span class="label center">Tickets</span></div>
  <div class="tab all"><span class="label center">All tickets</span></div>
  <div class="tab mine"><span class="label center">My tickets</span></div>
</nav>

<svg class="filter-icon" viewBox="0 0 20 20" fill="none" stroke="#1f2b2b" stroke-width="1.6">
  <path d="M3 2v16M10 2v16M17 2v16"/>
  <circle cx="3" cy="12" r="2" fill="#f8fce7"/><circle cx="10" cy="7" r="2" fill="#f8fce7"/><circle cx="17" cy="12" r="2" fill="#f8fce7"/>
</svg>

<section class="table">
  <div class="row head">
    <span class="cell check"></span>
    <svg class="cell star" viewBox="0 0 14 14" fill="none" stroke="#1f2b2b" stroke-width="1"><path d="M7 1l1.8 3.8 4.1.5-3 2.8.8 4.1L7 10.2 3.3 12.2l.8-4.1-3-2.8 4.1-.5z"/></svg>
    <span class="cell contact" style="font-size:12px"><span class="label">Contact</span></span>
    <span class="cell date"><span class="label">Date</span></span>
    <span class="cell num" style="color:var(--ink)"><span class="label">N°</span></span>
    <span class="cell subject"><span class="label">Subject</span></span>
    <span class="cell state"><span class="label">State</span></span>
    <span class="cell group"><span class="label">Group</span></span>
    <span class="cell agent"><span class="label">Agent</span></span>
    <span class="cell priority"><span class="label">Priority</span></span>
  </div>

  <div class="row" style="top:29px">
    <span class="cell check"></span>
    <svg class="cell star" viewBox="0 0 14 14" fill="none" stroke="#1f2b2b" stroke-width="1"><path d="M7 1l1.8 3.8 4.1.5-3 2.8.8 4.1L7 10.2 3.3 12.2l.8-4.1-3-2.8 4.1-.5z"/></svg>
    <span class="cell initials"><span class="label center">NW</span></span>
    <span class="cell contact"><span class="label">Nora Whitfield</span></span>
    <span class="cell date"><span class="label">Januari 2018 17:00</span></span>
    <span class="cell num"><span class="label">#10</span></span>
    <span class="cell subject"><span class="label">I can't reset my password</span></span>
    <span class="cell state"><span class="label">Past due</span></span>
    <span class="cell group"><span class="label">Sales</span></span>
    <span class="cell agent"><span class="label">Marcus</span></span>
    <span class="cell priority"><span class="label">Low</span></span>
  </div>

  <div class="row selected" style="top:85px">
    <span class="cell check"></span>
    <svg class="cell star" viewBox="0 0 14 14" fill="none" stroke="#1f2b2b" stroke-width="1"><path d="M7 1l1.8 3.8 4.1.5-3 2.8.8 4.1L7 10.2 3.3 12.2l.8-4.1-3-2.8 4.1-.5z"/></svg>
    <span class="cell initials"><span class="label center">RS</span></span>
    <span class="cell contact"><span class="label">Rania Solvik</span></span>
    <span class="cell date"><span class="label">Januari 2018 17:00</span></span>
    <span class="cell num"><span class="label">#15</span></span>
    <span class="cell subject"><span class="label">Forgot to CC</span></span>
    <span class="cell state"><span class="label">Past due</span></span>
    <span class="cell group"><span class="label">Sales</span></span>
    <span class="cell agent"><span class="label">Marcus</span></span>
    <span class="cell priority"><span class="label">Low</span></span>
  </div>

  <div class="row" style="top:141px">
    <span class="cell check"></span>
    <svg class="cell star" viewBox="0 0 14 14" fill="none" stroke="#1f2b2b" stroke-width="1"><path d="M7 1l1.8 3.8 4.1.5-3 2.8.8 4.1L7 10.2 3.3 12.2l.8-4.1-3-2.8 4.1-.5z"/></svg>
    <span class="cell initials"><span class="label center">OB</span></span>
    <span class="cell contact"><span class="label">Owen Brask</span></span>
    <span class="cell date"><span class="label">Januari 2018 17:00</span></span>
    <span class="cell num"><span class="label">#10</span></span>
    <span class="cell subject"><span class="label">Forgot to CC</span></span>
    <span class="cell state"><span class="label">Past due</span></span>
    <span class="cell group"><span class="label">Sales</span></span>
    <span class="cell agent"><span class="label">Marcus</span></span>
    <span class="cell priority"><span class="label">Low</span></span>
  </div>
</section>
</body>
</html>
```